IT Company that provides secure IT solutions and services to our customers

We need business cards and a logo for a new IT Solutions company just created based in Kuala Lumpur, Malaysia. But will also be serving other countries in the region. We provide secure data, voice solutions on mobile platforms. Our first offering is encrypted voice and data solutions for IOS, Android, Windows and BlackBerry devices.

Target Market(s)

large organizations Govt, Police, Defence, Anti-corruption, Legal, highly regulated industries such as Health-care, Financial, Banking, Insurance,

Industry/Entity Type

Information Technology

Contact Information for Business Card

VornaxIT (Logo - colour is ORBEL blue)Dariush Pelo Managing Director Vornax IT Sdn. Bhd.5th Floor, Block F, Wisma LBD,No.14 Jalan Seri Mewah,50470, Kuala LumpurMalaysia

Font styles to use
Sans Serif

Colors
3176b5
ec1f27
fbed22

Requirements
Must have
• VornaxIT all in Blue like ORBEL blue. A logo design perhaps a play of VI, K with a dangling T (colour can be any)
Nice to have
• I want a clean crisp card, not too busy, easy to read.

```html
<!DOCTYPE html>
<html lang="en">
<head>
<meta charset="utf-8">
<title>VornaxIT Business Cards</title>
<link href="https://fonts.googleapis.com/css2?family=Lato:wght@400;700;900&display=swap" rel="stylesheet">
<style>
  :root {
    --backdrop: #2b2b2d;
    --card: #262628;
    --card-panel: #2f2f31;
    --brand-blue: #1d97dd;
    --brand-blue-deep: #1583c6;
    --text-light: #f2f2f2;
    --text-soft: #d6d6d6;
  }
  * { margin: 0; padding: 0; box-sizing: border-box; }
  html, body {
    width: 1200px; height: 900px; overflow: hidden;
    background: var(--backdrop);
    font-family: "Lato", Arial, sans-serif;
  }
  .canvas { position: relative; width: 1200px; height: 900px; }

  .card {
    position: absolute;
    width: 640px; height: 366px;
    background: var(--card);
    box-shadow: 0 14px 30px rgba(0,0,0,.45);
    overflow: hidden;
  }
  .card--front { left: 100px; top: 60px; }
  .card--back  { left: 460px; top: 474px; }

  .brand { display: flex; flex-direction: column; align-items: center; }
  .brand__mark {
    width: 150px; height: 150px;
    background: linear-gradient(135deg, var(--brand-blue), var(--brand-blue-deep));
  }
  .brand__name {
    margin-top: 10px;
    color: var(--text-light);
    font-size: 34px; font-weight: 400; letter-spacing: 1px;
  }

  .card--front .brand { position: absolute; left: 0; right: 0; top: 62px; }
  .front__web {
    position: absolute; left: 0; right: 0; top: 290px;
    text-align: center; color: var(--text-light);
    font-size: 17px; font-weight: 700; letter-spacing: .6px;
  }

  .back__identity { position: absolute; left: 0; top: 46px; width: 330px; }
  .card--back .brand__mark { width: 128px; height: 128px; }
  .card--back .brand__name { font-size: 30px; margin-top: 8px; }
  .back__address {
    margin-top: 14px; text-align: center;
    color: var(--text-soft); font-size: 15px; line-height: 1.3; letter-spacing: .4px;
  }

  .back__panel {
    position: absolute; right: 0; top: 0;
    width: 318px; height: 100%;
    background: var(--card-panel);
    box-shadow: -6px 0 14px rgba(0,0,0,.35);
  }
  .nameband {
    margin-top: 30px; margin-left: 14px;
    background: var(--brand-blue);
    padding: 8px 14px 7px;
    color: #fff;
  }
  .nameband__name { font-size: 20px; line-height: 1.1; }
  .nameband__name strong { font-weight: 900; }
  .nameband__title { font-size: 14px; letter-spacing: 1px; line-height: 1.2; }

  .contacts { list-style: none; margin-top: 26px; }
  .contact {
    position: relative; height: 38px;
    display: flex; align-items: center;
  }
  .contact__tab {
    position: absolute; left: 0; height: 12px; top: 13px;
    background: var(--brand-blue);
  }
  .contact__icon {
    position: absolute; top: 3px;
    width: 32px; height: 32px; border-radius: 50%;
    background: var(--card-panel);
    border: 3px solid var(--brand-blue);
    display: flex; align-items: center; justify-content: center;
  }
  .contact__text {
    position: absolute; left: 120px;
    color: var(--text-light); font-size: 15px; letter-spacing: .4px;
  }
  .contact--phone .contact__tab { width: 40px; }
  .contact--phone .contact__icon { left: 36px; }
  .contact--mail .contact__tab { width: 60px; }
  .contact--mail .contact__icon { left: 56px; }
  .contact--web .contact__tab { width: 80px; }
  .contact--web .contact__icon { left: 76px; }
  .contact--phone .contact__text { top: -8px; }
</style>
</head>
<body>
<main class="canvas">

  <section class="card card--front" aria-label="Card front">
    <div class="brand">
      <div class="brand__mark"></div>
      <div class="brand__name">VornaxIT</div>
    </div>
    <div class="front__web">www.vornaxit.com</div>
  </section>

  <section class="card card--back" aria-label="Card back">
    <div class="back__identity">
      <div class="brand">
        <div class="brand__mark"></div>
        <div class="brand__name">VornaxIT</div>
      </div>
      <p class="back__address">
        Sdn. Bhd.5th Floor, Block F, Wisma LBD,<br>
        No.14 Jalan Seri Mewah,50470,<br>
        Kuala Lumpur Malaysia
      </p>
    </div>

    <div class="back__panel">
      <div class="nameband">
        <div class="nameband__name"><strong>Dariush</strong> Pelo</div>
        <div class="nameband__title">MANAGING DIRECTOR</div>
      </div>

      <ul class="contacts">
        <li class="contact contact--phone">
          <span class="contact__tab"></span>
          <span class="contact__icon">
            <svg width="16" height="14" viewBox="0 0 16 14" aria-hidden="true">
              <path d="M1 4 Q8 -1 15 4 L13 6 L11 4.5 L5 4.5 L3 6 Z" fill="#fff"/>
              <rect x="3" y="7" width="10" height="6" rx="1" fill="#fff"/>
            </svg>
          </span>
          <span class="contact__text">000 .1234 .5678</span>
        </li>
        <li class="contact contact--mail">
          <span class="contact__tab"></span>
          <span class="contact__icon">
            <svg width="16" height="12" viewBox="0 0 16 12" aria-hidden="true">
              <rect x="1" y="1" width="14" height="10" fill="#fff"/>
              <path d="M1 1 L8 7 L15 1" fill="none" stroke="#2f2f31" stroke-width="1.4"/>
            </svg>
          </span>
          <span class="contact__text">contact@vornaxit.com</span>
        </li>
        <li class="contact contact--web">
          <span class="contact__tab"></span>
          <span class="contact__icon">
            <svg width="16" height="16" viewBox="0 0 16 16" aria-hidden="true">
              <g fill="none" stroke="#fff" stroke-width="1.3">
                <circle cx="8" cy="8" r="6.5"/>
                <ellipse cx="8" cy="8" rx="3" ry="6.5"/>
                <line x1="1.5" y1="8" x2="14.5" y2="8"/>
                <line x1="8" y1="1.5" x2="8" y2="14.5"/>
              </g>
            </svg>
          </span>
          <span class="contact__text">www.vornaxit.com</span>
        </li>
      </ul>
    </div>
  </section>

</main>
</body>
</html>
```